Business Card Design

Very plain simple card, Plain modern font. Background. Grey fading to black. Large Bright lime green text. Saying.

TWR-ZA.COM

Small other details in white text.

Irish Horse Sales . Livery . Stud . Shows

Mark Dabrowski
TWR
Birch Lodge
Carrowmede Lane
Thistlecombe
Lincolnshire
LN4 7JX

Email. Twrzap@mailvale.co.uk
Tel. 07482 936504

Industry/Entity Type

Business

Contact Information for Business Card

As below

```html
<!DOCTYPE html>
<html lang="en">
<head>
<meta charset="utf-8">
<title>TWR-ZA.COM – Business Card</title>
<link rel="stylesheet" href="https://fonts.googleapis.com/css2?family=Titillium+Web:wght@300;400;600;700&display=swap">
<style>
  :root {
    --lime: #7cc242;
    --white: #ffffff;
    --text-soft: #e8e8e8;
    --frame: #1c1c1c;
    --bg-light: #5c5c5c;
    --bg-mid: #3a3a3a;
    --bg-dark: #101010;
  }
  html, body {
    margin: 0;
    padding: 0;
    width: 1200px;
    height: 791px;
    overflow: hidden;
    background: var(--bg-dark);
  }
  .card {
    position: relative;
    width: 1200px;
    height: 791px;
    overflow: hidden;
    font-family: "Titillium Web", "Helvetica Neue", Arial, sans-serif;
    background:
      radial-gradient(ellipse 110% 95% at 30% 10%, var(--bg-light) 0%, var(--bg-mid) 45%, var(--bg-dark) 100%);
  }
  .card__frame {
    position: absolute;
    left: 23px;
    top: 21px;
    width: 1154px;
    height: 747px;
    border: 1.5px solid var(--frame);
    box-sizing: border-box;
  }
  .brand {
    position: absolute;
    right: 54px;
    top: 177px;
    margin: 0;
    font-size: 88px;
    line-height: 1;
    font-weight: 700;
    color: var(--lime);
    letter-spacing: 0.5px;
  }
  .brand__domain {
    font-size: 64px;
  }
  .person {
    position: absolute;
    right: 59px;
    top: 313px;
    margin: 0;
    font-size: 58px;
    line-height: 1;
    font-weight: 400;
    color: var(--white);
  }
  .services {
    position: absolute;
    right: 55px;
    top: 382px;
    margin: 0;
    text-align: right;
    font-size: 28px;
    line-height: 35px;
    font-weight: 300;
    color: var(--text-soft);
  }
  .contact {
    position: absolute;
    right: 89px;
    top: 479px;
    margin: 0;
    text-align: right;
    font-style: normal;
    font-size: 23px;
    line-height: 34px;
    font-weight: 400;
    color: var(--text-soft);
  }
  .contact__place {
    font-weight: 600;
    color: var(--white);
  }
  .contact__phone,
  .contact__email {
    margin-top: 19px;
  }
  .contact__rule {
    position: absolute;
    left: 1143px;
    top: 477px;
    width: 9px;
    height: 204px;
    background: var(--lime);
  }
</style>
</head>
<body>
  <main class="card">
    <div class="card__frame"></div>

    <h1 class="brand">TWR-ZA<span class="brand__domain">.COM</span></h1>

    <h2 class="person">Mark Dabrowski</h2>

    <p class="services">Irish Horse Sales<br>Livery . Stud . Shows</p>

    <address class="contact">
      <div class="contact__place">Birch Lodge</div>
      <div>Carrowmede Lane, Thistlecombe</div>
      <div>Lincolnshire, LN4 7JX</div>
      <div class="contact__phone">07482 936504</div>
      <div class="contact__email">Twrzap@mailvale.co.uk</div>
    </address>
    <div class="contact__rule"></div>
  </main>
</body>
</html>
```